依頼詳細
神奈川県横浜市に2店舗展開する美容室です。

今年で4回目のクリスマスDM依頼となります。

小さいお子様から70代ぐらいの方まで幅広い世代にご利用いただいております。
なかでも30代40代の美意識の高い大人の女性をメインターゲットにしています。

2店舗ともそれぞれサロンの雰囲気が異なりますので、
ぜひHPを参考にご覧ください。

今年もクリスマスDMのポストカードデザインをお願いいたします。
2店舗同じものを使いたいと思っています。

美容室ですが、美容室っぽさはデザインの中に取り込まなくても結構です。

イメージ的には、
堅苦しくなく、
家族や友人から送られてきたのかな??
と感じるような、
女性目線のシンプルかつオシャレなデザインが希望です。

また、オリジナル性を重視しますので、
ロゴもしくは店名(moal)をデザインの中に取り入れていただきたいです。

過去の作品なども参考にしていただけたらと思います。

締切日が短く恐縮ではございますが、
宜しくお願いいたします。
記載項目
表面(切手を貼る側)デザインにコメント・年末年始のお休みのお知らせ・2店舗の店名住所電話番号・URLの記載をお願いします。手書きコメントスペースがほしいです。
【コメント】日頃のご愛顧、誠にありがとうございます。皆様の笑顔の為に素敵なヘアデザインと最高の満足をお届けできるように、技術の向上とサービスに努めてまいります。moalスタッフ一同、心よりお待ちしております。
【年末年始休み】12/25(火)定休日 26(水)~30(日)通常営業 31(月)~1/4(金)正月休み 5(土)より 通常営業
【住所など】moalPLUS 横浜市西区架空町3-8-2-1F TEL 045-555-0187 lumio by moal 横浜市中区仮名町2-46架空ステラビル1F TEL045-323-9807
【URL】http://moal.example
裏面:ロゴもしくは店名(moal)イラスト
希望イメージ
シンプル 複雑
単色 カラフル
暗い 明るい
日常 高級
遊び心 厳粛
未来的 伝統的
女性的 男性的
希望する色
設定なし
納品ファイル
• 高解像度JPG (.jpg)
• イラストレーター形式 (.ai)
補足説明
印刷を「プリモア」さんにお願いを予定しています。入稿前チェックガイドのご確認よろしくお願い致します。
https://help.primoa.example/guide/data-check-guide/?_ga=1.000000000.000000000.0000000000
■ 選んだ理由

全スタッフによる投票の結果で決めさせていただきました。
素敵なデザインありがとうございました。

■ 提案者全員のお礼・コメント

今年もたくさん素敵なデザイン提案誠に、ありがとうございました。
選定にお時間頂いてしまい申し訳ございませんでした。
機会がございましたら、今後もよろしくお願い致します。

```html
<!DOCTYPE html>
<html lang="ja">
<head>
<meta charset="utf-8">
<title>moal 年末年始のお休みのお知らせ</title>
<link rel="stylesheet" href="https://fonts.googleapis.com/css2?family=Noto+Sans+JP:wght@400;500;700&display=swap">
<style>
  :root {
    --accent-red: #c3262c;
    --ink: #333333;
    --ink-soft: #555555;
    --rule-grey: #9a9a9a;
    --paper: #ffffff;
  }
  html, body {
    margin: 0;
    padding: 0;
    width: 814px;
    height: 1200px;
    overflow: hidden;
    background: var(--paper);
  }
  .postcard {
    position: relative;
    width: 814px;
    height: 1200px;
    font-family: "Noto Sans JP", sans-serif;
    color: var(--ink);
    overflow: hidden;
  }
  .postcard-label {
    position: absolute;
    top: 30px;
    left: 360px;
    font-size: 22px;
    letter-spacing: 1px;
    color: var(--ink-soft);
  }
  .address-frame {
    position: absolute;
    top: 0;
    left: 0;
  }
  .notice-rule {
    position: absolute;
    top: 644px;
    left: 54px;
    width: 706px;
    height: 3px;
    background: var(--accent-red);
  }
  .notice-title {
    position: absolute;
    top: 672px;
    left: 0;
    width: 814px;
    text-align: center;
    margin: 0;
    font-size: 28px;
    font-weight: 500;
    letter-spacing: 1px;
    color: var(--ink);
  }
  .greeting {
    position: absolute;
    top: 744px;
    left: 98px;
    margin: 0;
    font-size: 19px;
    line-height: 32px;
    color: var(--ink);
  }
  .holiday-schedule {
    position: absolute;
    top: 938px;
    left: 98px;
    margin: 0;
    font-size: 24px;
    font-weight: 700;
    line-height: 46px;
    color: var(--ink);
  }
  .holiday-schedule .gap { display: inline-block; width: 18px; }
  .shop-rule {
    position: absolute;
    top: 1040px;
    left: 84px;
    width: 646px;
    height: 1px;
    background: var(--rule-grey);
  }
  .shop-list {
    position: absolute;
    top: 1054px;
    left: 98px;
    margin: 0;
    padding: 0;
    list-style: none;
  }
  .shop { margin-bottom: 10px; }
  .shop-name {
    font-size: 17px;
    font-weight: 700;
    line-height: 24px;
    color: var(--ink);
  }
  .shop-detail {
    font-size: 16px;
    line-height: 24px;
    color: var(--ink);
  }
  .url-band {
    position: absolute;
    left: 0;
    top: 1158px;
    width: 814px;
    height: 42px;
    background: var(--accent-red);
    color: var(--paper);
    text-align: center;
    font-size: 28px;
    font-weight: 700;
    line-height: 42px;
    letter-spacing: 1px;
  }
</style>
</head>
<body>
<main class="postcard">
  <div class="postcard-label">post card</div>

  <svg class="address-frame" width="814" height="220" viewBox="0 0 814 220" aria-hidden="true">
    <g fill="none" stroke="#333333" stroke-width="3">
      <rect class="stamp-box" x="56" y="60" width="112" height="143"/>
      <rect x="312" y="92" width="52" height="58"/>
      <rect x="370" y="92" width="52" height="58"/>
      <rect x="428" y="92" width="52" height="58"/>
      <rect x="514" y="92" width="52" height="58"/>
      <rect x="572" y="92" width="52" height="58"/>
      <rect x="630" y="92" width="52" height="58"/>
      <rect x="688" y="92" width="52" height="58"/>
      <line x1="484" y1="121" x2="510" y2="121"/>
    </g>
  </svg>

  <div class="notice-rule"></div>
  <h1 class="notice-title">年末年始のお休みのお知らせ</h1>

  <p class="greeting">
    日頃のご愛顧、誠にありがとうございます。<br>
    皆様の笑顔の為に素敵なヘアデザインと最高の満足を<br>
    お届けできるように、技術の向上とサービスに努めてまいります。<br>
    moalスタッフ一同、心よりお待ちしております。
  </p>

  <p class="holiday-schedule">
    12/25(火)定休日<span class="gap"></span>26(水)〜30(日)通常営業<br>
    12/31(月)〜 1/4(金)正月休み<span class="gap"></span>1/5(土)より通常営業
  </p>

  <div class="shop-rule"></div>
  <ul class="shop-list">
    <li class="shop">
      <div class="shop-name">moalPLUS</div>
      <div class="shop-detail">横浜市西区架空町3-8-2-1F　TEL 045-555-0187</div>
    </li>
    <li class="shop">
      <div class="shop-name">lumio by moal</div>
      <div class="shop-detail">横浜市中区仮名町2-46架空ステラビル1F TEL045-555-0142</div>
    </li>
  </ul>

  <div class="url-band">http://moal.example</div>
</main>
</body>
</html>
```